Kestrelwood Pathways Agency business cards

Australian company about to start offering its services. We recruit international students to come to study English, vocational education and postgraduate courses in Australia. We help them find the institution and select the right city they want to come to Australia. We are a young, online oriented and supportive agency. Our clients are between 18 and 35 years old, mainly University students, young professionals or people with work experience. We provide much more information that any other agency offer. We administrate a Facebook group with more than 11.000 members that daily ask questions about general information when coming to Australia, while they are here and even after they leave the country

Target Market(s)

International students from South America, Central America and Europe

Industry/Entity Type

Student

Contact Information for Business Card

Tomas Brevik
Managing Director
tomas@velmorin.com.au
www.velmorin.com.au
+61 491058263
Carrowdale, Australia

Font styles to use
Serif
Sans Serif

Colors

Designer to choose colors to be used in the design.

Requirements
Must have
• Horizontal design
• Standard business card size and shape. If font uses green or yellow colours, they will have to match the ones from the logo
Nice to have
• UPDATE: Use the contents of the green image to design one of the card sides. Use our logo in the background of that side as watermark.
• Passport image, or immigration stamps. A picture of the Yarra River (from Melbourne) would be cool as well.
Should not have
• Non-standard business card size and shape
• Not black as the background colour of any sides as we are not a VIP agency or a hight class service. We are orientes to young people and they like colours, pictures, something attractive.
• Vertical design
• NO YELLOW or BLACK AS THE BACKGROUND COLOUR OF ANY SIDE OF THE BIZ CARD

```html
<!DOCTYPE html>
<html lang="en">
<head>
<meta charset="utf-8">
<title>Kestrelwood Pathways Agency – Business Cards</title>
<link rel="stylesheet" href="https://fonts.googleapis.com/css2?family=Lato:ital,wght@0,400;0,700;0,900;1,700&display=swap">
<style>
  :root {
    --green: #11673f;
    --yellow: #e8b920;
    --white: #ffffff;
    --stage: #d6d8d7;
    --card-w: 600px;
    --card-h: 343px;
  }
  * { margin: 0; padding: 0; box-sizing: border-box; }
  html, body { width: 1200px; height: 900px; overflow: hidden; }
  body { background: var(--stage); font-family: "Lato", sans-serif; position: relative; }

  .card {
    position: absolute;
    width: var(--card-w);
    height: var(--card-h);
    border-radius: 22px;
    overflow: hidden;
    box-shadow: 0 10px 28px rgba(0,0,0,0.18);
  }

  /* Back side */
  .card-back { left: 520px; top: 70px; background: var(--green); }
  .card-back .brand {
    position: absolute; left: 0; right: 0; top: 120px;
    display: flex; align-items: center; justify-content: center; gap: 14px;
  }
  .brand-dot { width: 26px; height: 26px; border-radius: 50%; background: var(--yellow); flex: none; }
  .brand-name { font-weight: 900; font-size: 46px; letter-spacing: 0.5px; line-height: 1; }
  .card-back .brand-name { color: var(--white); }
  .tagline {
    position: absolute; left: 0; right: 0; top: 232px; text-align: center;
    color: var(--white); font-style: italic; font-weight: 700; font-size: 17px; letter-spacing: 1px;
  }

  /* Front side */
  .card-front { left: 80px; top: 460px; background: var(--white); }
  .front-waves { position: absolute; inset: 0; }
  .card-front .brand {
    position: absolute; left: 70px; top: 52px;
    display: flex; align-items: center; gap: 12px;
  }
  .card-front .brand-name { color: var(--green); font-size: 42px; }
  .identity { position: absolute; right: 40px; top: 112px; text-align: right; }
  .identity-name { color: var(--green); font-weight: 900; font-size: 22px; letter-spacing: 0.5px; text-transform: uppercase; }
  .identity-role { color: var(--yellow); font-weight: 700; font-size: 13px; letter-spacing: 1px; text-transform: uppercase; margin-top: 2px; }

  .contacts { position: absolute; right: 22px; top: 248px; list-style: none; }
  .contact {
    display: flex; align-items: center; justify-content: flex-end; gap: 10px;
    color: var(--white); font-size: 14px; height: 22px;
  }
  .contact-icon { width: 18px; height: 18px; flex: none; }
</style>
</head>
<body>

<section class="card card-back" aria-label="Business card back">
  <div class="brand">
    <span class="brand-dot"></span>
    <span class="brand-name">Kestrelwood</span>
  </div>
  <p class="tagline">Contigo en cada paso!</p>
</section>

<section class="card card-front" aria-label="Business card front">
  <svg class="front-waves" viewBox="0 0 600 343" preserveAspectRatio="none" aria-hidden="true">
    <path fill="var(--green)"  d="M0,100 C150,130 300,215 600,185 L600,343 L0,343 Z"/>
    <path fill="var(--white)"  d="M0,128 C160,160 310,230 600,200 L600,343 L0,343 Z"/>
    <path fill="var(--yellow)" d="M0,143 C170,180 320,240 600,212 L600,343 L0,343 Z"/>
    <path fill="var(--white)"  d="M0,172 C180,205 330,252 600,226 L600,343 L0,343 Z"/>
    <path fill="var(--green)"  d="M0,192 C190,222 340,262 600,238 L600,343 L0,343 Z"/>
  </svg>

  <div class="brand">
    <span class="brand-dot"></span>
    <span class="brand-name">Kestrelwood</span>
  </div>

  <div class="identity">
    <p class="identity-name">Tomas Brevik</p>
    <p class="identity-role">Managing Director</p>
  </div>

  <ul class="contacts">
    <li class="contact">
      <span>Carrowdale, Australia</span>
      <svg class="contact-icon" viewBox="0 0 18 18" aria-hidden="true">
        <rect width="18" height="18" rx="4" fill="var(--yellow)"/>
        <path d="M9 3.5a3.6 3.6 0 0 0-3.6 3.6c0 2.7 3.6 7 3.6 7s3.6-4.3 3.6-7A3.6 3.6 0 0 0 9 3.5z" fill="var(--green)"/>
        <circle cx="9" cy="7.1" r="1.3" fill="var(--yellow)"/>
      </svg>
    </li>
    <li class="contact">
      <span>+61 491 058 263</span>
      <svg class="contact-icon" viewBox="0 0 18 18" aria-hidden="true">
        <rect width="18" height="18" rx="4" fill="var(--yellow)"/>
        <path d="M5.2 4c.5-.4 1.2-.3 1.5.2l1 1.7c.3.5.1 1-.3 1.3l-.6.4c.5 1.2 1.4 2.1 2.6 2.6l.4-.6c.3-.4.9-.6 1.3-.3l1.7 1c.5.3.6 1 .2 1.5l-.7.8c-.5.5-1.3.7-2 .4-2.6-1-4.5-2.9-5.5-5.5-.3-.7-.1-1.5.4-2z" fill="var(--green)"/>
      </svg>
    </li>
    <li class="contact">
      <span>tomas@velmorin.com.au</span>
      <svg class="contact-icon" viewBox="0 0 18 18" aria-hidden="true">
        <rect width="18" height="18" rx="4" fill="var(--yellow)"/>
        <rect x="3.5" y="5" width="11" height="8" rx="1" fill="none" stroke="var(--green)" stroke-width="1.4"/>
        <path d="M3.8 5.4 9 9.5l5.2-4.1" fill="none" stroke="var(--green)" stroke-width="1.4"/>
      </svg>
    </li>
    <li class="contact">
      <span>www.velmorin.com.au</span>
      <svg class="contact-icon" viewBox="0 0 18 18" aria-hidden="true">
        <rect width="18" height="18" rx="4" fill="var(--yellow)"/>
        <g fill="none" stroke="var(--green)" stroke-width="1.2">
          <circle cx="9" cy="9" r="5"/>
          <ellipse cx="9" cy="9" rx="2.2" ry="5"/>
          <path d="M4 9h10M5 6.5h8M5 11.5h8"/>
        </g>
      </svg>
    </li>
  </ul>
</section>

</body>
</html>
```